The Web Promotion Playbook for Yard & Patio Construction Crews

We need a book cover design that is for a book targeting landscape and outdoor living contractors that helps them grow their business using online marketing.

We run a business focused on this industry so you can see what we do: https://yardcrewgrowthworks.com/

The title is: The Web Promotion Playbook for Yard & Patio Construction Crews

The author is: Trent Varnholm
Some drafts have been done however they're still looking basic and somewhat amateur, we're looking for something that will stand out.

Target Market(s)

Landscape, Hardscape and Outdoor Living Contractors and Business Owners

Industry/Entity Type

Online Marketing

Font styles to use
Serif
Sans Serif

Requirements
Must have
• The part of the title that should stand out the most is the text "Web Promotion Playbook".
Should not have
• The color red

```html
<!DOCTYPE html>
<html lang="en">
<head>
<meta charset="utf-8">
<title>The Web Promotion Playbook for Yard &amp; Patio Construction Crews — Trent Varnholm</title>
<link rel="stylesheet" href="https://fonts.googleapis.com/css2?family=Bebas+Neue&display=swap">
<style>
  :root {
    --page-bg: #ffffff;
    --cover-yellow-core: #f1df00;
    --cover-yellow-edge: #e4b521;
    --forest-green: #0d2e17;
    --title-white: #f3f3f3;
  }
  html, body {
    margin: 0;
    padding: 0;
    width: 1071px;
    height: 1200px;
    overflow: hidden;
    background: var(--page-bg);
  }
  .canvas {
    position: relative;
    width: 1071px;
    height: 1200px;
  }
  .book-cover {
    position: absolute;
    left: 135px;
    top: 25px;
    width: 800px;
    height: 1150px;
    display: block;
  }
  .cover-text {
    font-family: "Bebas Neue", "Oswald", sans-serif;
  }
  .title-line--dark {
    fill: var(--forest-green);
  }
  .title-line--light {
    fill: var(--title-white);
    stroke: var(--forest-green);
    stroke-width: 3;
    paint-order: stroke;
  }
  .author-band {
    fill: var(--forest-green);
  }
  .author-name {
    fill: var(--title-white);
    letter-spacing: 6px;
  }
</style>
</head>
<body>
<main class="canvas">
  <svg class="book-cover" viewBox="0 0 800 1150" xmlns="http://www.w3.org/2000/svg" role="group" aria-label="Book cover: The Web Promotion Playbook for Yard and Patio Construction Crews by Trent Varnholm">
    <defs>
      <radialGradient id="cover-glow" cx="50%" cy="38%" r="70%">
        <stop offset="0%" stop-color="var(--cover-yellow-core)"/>
        <stop offset="100%" stop-color="var(--cover-yellow-edge)"/>
      </radialGradient>
    </defs>

    <rect class="cover-ground" x="0" y="0" width="800" height="1150" fill="url(#cover-glow)"/>

    <g class="cover-text title-block">
      <text class="title-line title-line--light" x="400" y="150" font-size="120" text-anchor="middle">THE</text>
      <text class="title-line title-line--dark title-key" x="60" y="291" font-size="165" textLength="680" lengthAdjust="spacingAndGlyphs">WEB PROMOTION</text>
      <text class="title-line title-line--dark title-key" x="60" y="515" font-size="280" textLength="680" lengthAdjust="spacingAndGlyphs">PLAYBOOK</text>
      <text class="title-line title-line--light" x="60" y="638" font-size="135" textLength="680" lengthAdjust="spacingAndGlyphs">FOR YARD &amp; PATIO</text>
      <text class="title-line title-line--light" x="60" y="779" font-size="165" textLength="680" lengthAdjust="spacingAndGlyphs">CONSTRUCTION</text>
      <text class="title-line title-line--light" x="400" y="934" font-size="185" text-anchor="middle">CREWS</text>
    </g>

    <rect class="author-band" x="0" y="1025" width="800" height="125"/>
    <text class="cover-text author-name" x="400" y="1110" font-size="78" text-anchor="middle">TRENT VARNHOLM</text>
  </svg>
</main>
</body>
</html>
```